Calder Ridge Minerals

Looking for a cool, glossy business card...white with our logo on one side and then the a smaller version of the logo on the other side (top left hand corner) and then the name and position of the person next to it, and then the office address and email address on the bottom left hand corner and the phone numbers & email address on the bottom right hand corner. I have the logo already...can pass it on when you're ready.

```html
<!DOCTYPE html>
<html lang="en">
<head>
<meta charset="utf-8">
<title>Calder Ridge Minerals – Business Card</title>
<link href="https://fonts.googleapis.com/css2?family=Cinzel:wght@500&family=Poppins:wght@400&display=swap" rel="stylesheet">
<style>
  :root {
    --bg: #e6e9ea;
    --card: #ffffff;
    --ink: #222426;
    --red: #c0141c;
    --blue: #1a1fd0;
    --edge: #d4d7d8;
  }
  * { margin: 0; padding: 0; box-sizing: border-box; }
  html, body { width: 1200px; height: 900px; overflow: hidden; background: var(--bg); }
  .canvas { position: relative; width: 1200px; height: 900px; }
  .card {
    position: absolute; left: 260px; width: 680px; height: 389px;
    background: var(--card);
    box-shadow: 0 2px 0 var(--edge), 0 10px 24px rgba(0,0,0,0.08);
  }
  .card--front { top: 44px; }
  .card--back { top: 467px; }

  .brand {
    display: flex; align-items: center;
    font-family: "Cinzel", serif; font-weight: 500; color: var(--ink);
    letter-spacing: 0.04em; white-space: nowrap;
  }
  .brand__dot { flex: none; background: var(--ink); }

  /* front */
  .card--front .brand {
    position: absolute; left: 0; right: 0; top: 0; bottom: 0;
    justify-content: center; gap: 16px; font-size: 34px;
  }
  .card--front .brand__dot { width: 14px; height: 14px; }

  /* back */
  .card--back .brand { position: absolute; left: 40px; top: 50px; gap: 10px; font-size: 21px; }
  .card--back .brand__dot { width: 10px; height: 10px; }

  .person { position: absolute; right: 44px; top: 40px; text-align: right; }
  .person__name { font-family: "Cinzel", serif; font-weight: 500; font-size: 26px; color: var(--red); letter-spacing: 0.03em; }
  .person__role { font-family: "Poppins", sans-serif; font-size: 14px; color: var(--blue); letter-spacing: 0.04em; }

  .divider { position: absolute; left: 40px; right: 44px; top: 218px; height: 2px; background: var(--red); }

  .contact { position: absolute; top: 240px; font-family: "Poppins", sans-serif; font-size: 15px; color: var(--ink); line-height: 1.55; }
  .contact--address { left: 40px; }
  .contact--lines { right: 44px; }
  .contact__row { display: flex; align-items: center; gap: 8px; }
  .contact__row svg { width: 18px; height: 18px; flex: none; }
</style>
</head>
<body>
<div class="canvas">

  <section class="card card--front">
    <div class="brand"><span class="brand__dot"></span><span>Calder Ridge Minerals</span></div>
  </section>

  <section class="card card--back">
    <div class="brand"><span class="brand__dot"></span><span>Calder Ridge Minerals</span></div>

    <div class="person">
      <div class="person__name">OWEN R HALE</div>
      <div class="person__role">MANAGER</div>
    </div>

    <div class="divider"></div>

    <div class="contact contact--address">
      <div>PO BOX 48 Harlow Lane</div>
      <div>2nd street Ashford</div>
      <div class="contact__row">
        <svg viewBox="0 0 18 18"><circle cx="9" cy="9" r="9" fill="#1a1fd0"/><rect x="4.5" y="6" width="9" height="6.5" fill="none" stroke="#fff" stroke-width="1.2"/><path d="M4.5 6 L9 9.6 L13.5 6" fill="none" stroke="#fff" stroke-width="1.2"/></svg>
        <span>info@calderridge-mail.com</span>
      </div>
    </div>

    <div class="contact contact--lines">
      <div class="contact__row">
        <svg viewBox="0 0 18 18"><circle cx="9" cy="9" r="9" fill="#1a1fd0"/><path d="M6 5 L7.8 5 L8.4 7.4 L7.3 8.2 Q8.3 10.3 10 11 L10.8 9.8 L13 10.4 L13 12.2 Q9 12.8 6.8 10.4 Q5 8.2 6 5 Z" fill="#fff"/></svg>
        <span>555-014-2280</span>
      </div>
      <div class="contact__row">
        <svg viewBox="0 0 18 18"><circle cx="9" cy="9" r="9" fill="#1a1fd0"/><rect x="6" y="4.5" width="6" height="9" rx="1" fill="none" stroke="#fff" stroke-width="1.2"/></svg>
        <span>555-014-2281</span>
      </div>
      <div class="contact__row">
        <svg viewBox="0 0 18 18"><circle cx="9" cy="9" r="9" fill="#1a1fd0"/><rect x="4.5" y="6" width="9" height="6.5" fill="none" stroke="#fff" stroke-width="1.2"/><path d="M4.5 6 L9 9.6 L13.5 6" fill="none" stroke="#fff" stroke-width="1.2"/></svg>
        <span>info@calderridge-mail.com</span>
      </div>
    </div>
  </section>

</div>
</body>
</html>
```